Copper Ridge Business Cards For New Startup

I am looking for you to design some business cards for a new startup https://copperridgehub.example. I have supplied logo, brand guidelines and our signatures as a guide.

We need this to reflect the brand guidelines and the website for brand consistency,

What is Copper Ridge?

Mallorca's Business Growth Community
Join your new business community full of passionate entrepreneurs who
love to solve problems and help each other grow together!

Any questions you can ask.

Target Market(s)

Business to Business

Contact Information for Business Card

These are attached (signatures) to the job

Font styles to use
Other font styles liked:
• Open Sans

Requirements
Must have
• Match design guidelines
Nice to have
• Photos of our faces so people remember us

```html
<!DOCTYPE html>
<html lang="en">
<head>
<meta charset="utf-8">
<title>Copper Ridge Business Cards</title>
<link href="https://fonts.googleapis.com/css2?family=Montserrat:wght@600;700&family=Open+Sans:wght@300;400;600&display=swap" rel="stylesheet">
<style>
  :root {
    --backdrop: #272a55;
    --olive: #656b2e;
    --paper: #ffffff;
    --ink-soft: #5b5b5b;
    --ring: #d9d8c8;
    --photo-a: #c9b8a6;
    --photo-b: #4c5a78;
  }
  * { box-sizing: border-box; margin: 0; padding: 0; }
  html, body { width: 1200px; height: 675px; overflow: hidden; }
  body {
    background: var(--backdrop);
    display: flex;
    align-items: center;
    justify-content: center;
    gap: 80px;
    font-family: "Open Sans", sans-serif;
  }
  .card {
    position: relative;
    width: 300px;
    height: 480px;
    overflow: hidden;
  }

  /* Front */
  .card-front { background: var(--paper); }
  .edge-strip {
    position: absolute; left: 0; top: 18px;
    width: 12px; height: 300px;
    background: var(--olive);
  }
  .brand {
    position: absolute; top: 44px; left: 0; right: 0;
    display: flex; flex-direction: column; align-items: center; gap: 14px;
  }
  .brand-square {
    width: 72px; height: 72px; border-radius: 12px;
    background: var(--olive);
  }
  .brand-name {
    font-family: "Montserrat", sans-serif;
    font-weight: 600;
    font-size: 24px;
    letter-spacing: 0.5px;
    color: var(--olive);
    text-transform: uppercase;
  }
  .portrait-ring {
    position: absolute; left: 56px; top: 188px;
    width: 118px; height: 118px; border-radius: 50%;
    border: 4px solid var(--ring);
  }
  .portrait {
    position: absolute; left: 34px; top: 212px;
    width: 108px; height: 86px;
    background: linear-gradient(135deg, var(--photo-a), var(--photo-b));
  }
  .person {
    position: absolute; left: 150px; top: 194px; right: 8px;
  }
  .person-name {
    font-family: "Montserrat", sans-serif;
    font-weight: 700; font-size: 19px;
    color: var(--olive);
    line-height: 1.1;
    white-space: nowrap;
  }
  .person-role {
    margin-top: 4px;
    font-weight: 300; font-size: 12px;
    letter-spacing: 2px;
    color: var(--ink-soft);
    line-height: 1.3;
  }
  .contact-band {
    position: absolute; left: 0; right: 0; top: 318px;
    height: 86px;
    background: var(--olive);
    color: var(--paper);
    padding: 20px 0 0 30px;
    font-size: 13px;
    line-height: 22px;
  }
  .contact-band b { font-weight: 600; }
  .site-line {
    position: absolute; left: 0; right: 0; top: 416px;
    text-align: center;
    font-size: 13px;
    letter-spacing: 3px;
    color: var(--olive);
  }
  .social-row {
    position: absolute; left: 0; right: 0; top: 444px;
    display: flex; justify-content: center; gap: 8px;
  }
  .social-chip {
    width: 20px; height: 20px; border-radius: 5px;
    background: var(--olive);
  }

  /* Back */
  .card-back {
    background: var(--olive);
    display: flex; flex-direction: column; align-items: center;
    padding-top: 190px;
    color: var(--paper);
  }
  .back-name {
    font-family: "Montserrat", sans-serif;
    font-weight: 600; font-size: 26px;
    letter-spacing: 0.5px;
    text-transform: uppercase;
  }
  .back-site {
    margin-top: 10px;
    font-size: 12px;
    letter-spacing: 3px;
  }
</style>
</head>
<body>
  <section class="card card-front" aria-label="Business card front">
    <div class="edge-strip"></div>
    <div class="brand">
      <div class="brand-square"></div>
      <div class="brand-name">Copper Ridge</div>
    </div>
    <div class="portrait-ring"></div>
    <div class="portrait" role="img" aria-label="Portrait photo of Daniel Marsh"></div>
    <div class="person">
      <div class="person-name">Daniel Marsh</div>
      <div class="person-role">Founder &amp;<br>Growth Hacker</div>
    </div>
    <div class="contact-band">
      <div><b>M:</b> +34 611 482 907</div>
      <div><b>E:</b> dm@copperridgehub.example</div>
    </div>
    <div class="site-line">copperridgehub.example</div>
    <div class="social-row">
      <span class="social-chip"></span>
      <span class="social-chip"></span>
      <span class="social-chip"></span>
      <span class="social-chip"></span>
      <span class="social-chip"></span>
    </div>
  </section>

  <section class="card card-back" aria-label="Business card back">
    <div class="back-name">Copper Ridge</div>
    <div class="back-site">copperridgehub.example</div>
  </section>
</body>
</html>
```